Brackenridge Strength Studio Chronic Pain Flyer

Double sided DL flyer required to promote a strength training studio to sufferers of chronic pain. Flyer will be displayed in osteopathy, chiropractic and massage clinics. Flyer should be clean, professional and appeal to an older (40+) demographic.

Target Market(s)

Chronic pain sufferers. Age 40+

Industry/Entity Type

Health And Wellness

Colors

Designer to choose colors to be used in the design.

Requirements
Must have
• See attached files for text copy and logo. Image(s) of people strength training with a coach or personal trainer, as well as images depicting pain in common parts of the body (such as those pictured in the supplied mock up)
• website address: brackenridgestrengthstudio.example.com.au
• phone number : 0452 918 304
• Street address: 4/63 Juniper Hollow Rd, Brackenridge
Nice to have
• Images such as in the attached files.

```html
<!DOCTYPE html>
<html lang="en">
<head>
<meta charset="utf-8">
<title>Brackenridge Strength Studio – Chronic Pain Flyer</title>
<link rel="stylesheet" href="https://fonts.googleapis.com/css2?family=Open+Sans:wght@400;600;700;800&display=swap">
<style>
  :root {
    --stage: #9b9b9b;
    --paper: #ffffff;
    --red: #d0202a;
    --red-bright: #e3262e;
    --ink: #1e1e1e;
    --grey-text: #5b5b5b;
    --grey-line: #cfcfcf;
  }
  * { box-sizing: border-box; margin: 0; padding: 0; }
  html, body { width: 826px; height: 1200px; overflow: hidden; }
  body {
    background: var(--stage);
    font-family: "Open Sans", Arial, sans-serif;
    position: relative;
  }
  .flyer {
    position: absolute;
    top: 240px;
    width: 360px;
    height: 720px;
    background: var(--paper);
    overflow: hidden;
  }
  .flyer--front { left: 40px; }
  .flyer--back { left: 426px; }

  .layer { position: absolute; left: 0; top: 0; width: 360px; height: 720px; pointer-events: none; }
  .layer--base { z-index: 1; }
  .layer--lines { z-index: 4; }

  .brand {
    position: absolute;
    left: 0; right: 0;
    text-align: center;
    font-weight: 800;
    color: var(--grey-text);
    font-size: 21px;
    line-height: 24px;
    letter-spacing: 0.5px;
    text-transform: uppercase;
    z-index: 5;
  }
  .flyer--front .brand { top: 52px; }
  .flyer--back .brand { top: 40px; }

  .hex-field {
    position: absolute;
    left: 0; top: 130px; width: 360px; height: 460px;
    background: linear-gradient(180deg, #f4f4f4 0%, #e4e4e4 55%, #f1f1f1 100%);
    z-index: 0;
  }
  .headline--front {
    position: absolute;
    top: 218px; left: 0; right: 0;
    text-align: center;
    color: var(--red);
    font-weight: 700;
    font-size: 40px;
    line-height: 45px;
    letter-spacing: 0.5px;
    z-index: 5;
  }
  .photo { position: absolute; }
  .photo--shoulder {
    left: 60px; top: 360px; width: 270px; height: 220px;
    z-index: 2;
    background: radial-gradient(circle at 48% 28%, rgba(225,60,60,0.75) 0%, rgba(200,80,80,0.25) 16%, transparent 30%),
                linear-gradient(160deg, #d6d6d6 0%, #8d8d8d 50%, #bdbdbd 100%);
  }
  .photo--gym {
    left: 0; top: 60px; width: 360px; height: 246px;
    z-index: 0;
    background: linear-gradient(180deg, #7a1a1c 0%, #a82226 40%, #4a0b0d 100%);
  }
  .photo--knee {
    left: 85px; top: 368px; width: 190px; height: 170px;
    z-index: 2;
    background: radial-gradient(circle at 48% 52%, rgba(225,50,50,0.85) 0%, rgba(210,80,80,0.3) 18%, transparent 32%),
                linear-gradient(180deg, #a9a9a9 0%, #c9c9c9 55%, #ececec 100%);
  }

  .headline--back {
    position: absolute;
    top: 162px; left: 0; right: 0;
    text-align: center;
    color: #fff;
    font-weight: 700;
    font-size: 26px;
    line-height: 30px;
    letter-spacing: 0.5px;
    z-index: 5;
  }
  .tagline {
    position: absolute;
    top: 232px; left: 0; right: 0;
    text-align: center;
    color: #fff;
    font-size: 18px;
    z-index: 5;
  }
  .body-copy {
    position: absolute;
    left: 24px; right: 24px;
    font-size: 11.2px;
    line-height: 14px;
    color: var(--ink);
    text-align: justify;
    z-index: 5;
  }
  .body-copy--intro { top: 314px; }
  .body-copy--studio { top: 550px; }

  .contact-phone {
    position: absolute;
    top: 612px; left: 0; right: 0;
    display: flex; justify-content: center; align-items: center; gap: 12px;
    color: var(--red);
    font-weight: 600;
    font-size: 34px;
    line-height: 40px;
    z-index: 5;
  }
  .contact-phone svg { width: 28px; height: 28px; }
  .contact-address {
    position: absolute;
    top: 656px; left: 0; right: 0;
    display: flex; justify-content: center; align-items: center; gap: 8px;
    font-size: 13.5px;
    color: var(--ink);
    z-index: 5;
  }
  .contact-address svg { width: 11px; height: 13px; }
  .web-band {
    position: absolute;
    left: 0; bottom: 0; width: 360px; height: 38px;
    background: var(--red-bright);
    display: flex; justify-content: center; align-items: center; gap: 8px;
    color: #fff;
    font-size: 12.5px;
    z-index: 5;
  }
  .web-band svg { width: 12px; height: 12px; }
</style>
</head>
<body>

<!-- Front side -->
<section class="flyer flyer--front">
  <div class="hex-field" role="img" aria-label="Soft grey hexagon texture background"></div>
  <div class="photo photo--shoulder" role="img" aria-label="Black and white photo of a man holding his shoulder, pain area highlighted red"></div>
  <svg class="layer layer--lines" viewBox="0 0 360 720" aria-hidden="true">
    <path d="M0 0 H360 V115 Q180 175 0 140 Z" fill="#fff"/>
    <path d="M0 128 Q190 172 360 108" fill="none" stroke="var(--grey-line)" stroke-width="4"/>
    <path d="M0 140 Q180 178 360 118 L360 128 Q180 186 0 150 Z" fill="var(--red)"/>
    <path d="M0 590 Q180 540 360 565 V720 H0 Z" fill="#fff"/>
    <path d="M0 585 Q180 535 360 560 L360 568 Q180 545 0 595 Z" fill="var(--red)"/>
  </svg>
  <div class="brand">Brackenridge<br>Strength Studio</div>
  <h1 class="headline--front">HEALTH<br>THROUGH<br>STRENGTH</h1>
  <div class="contact-phone">
    <svg viewBox="0 0 28 28" aria-hidden="true"><circle cx="14" cy="14" r="12" fill="none" stroke="currentColor" stroke-width="2.4"/><path d="M9 8.5c1-1 2-1 2.6 0l1.2 2c.4.7.2 1.3-.4 1.8l-.7.6c.7 1.6 1.8 2.8 3.4 3.5l.6-.7c.5-.6 1.2-.8 1.8-.4l2 1.2c1 .6 1 1.6 0 2.6-1.4 1.3-3.2 1.4-5.6-.3-2.2-1.5-3.8-3.3-4.8-5.6-.9-2.1-.6-3.6.5-4.7z" fill="currentColor"/></svg>
    <span>0452 918 304</span>
  </div>
  <div class="contact-address">
    <svg viewBox="0 0 11 13" aria-hidden="true"><path d="M5.5 12.5S1 7.8 1 5a4.5 4.5 0 0 1 9 0c0 2.8-4.5 7.5-4.5 7.5z" fill="none" stroke="var(--red)" stroke-width="1.3"/><circle cx="5.5" cy="5" r="1.5" fill="var(--red)"/></svg>
    <span>4/63 Juniper Hollow Rd, Brackenridge</span>
  </div>
  <div class="web-band">
    <svg viewBox="0 0 12 12" aria-hidden="true"><circle cx="6" cy="6" r="5.2" fill="none" stroke="#fff" stroke-width="1"/><ellipse cx="6" cy="6" rx="2.3" ry="5.2" fill="none" stroke="#fff" stroke-width="1"/><path d="M0.8 6h10.4" stroke="#fff" stroke-width="1"/></svg>
    <span>www.brackenridgestrengthstudio.example.com.au</span>
  </div>
</section>

<!-- Back side -->
<section class="flyer flyer--back">
  <div class="photo photo--gym" role="img" aria-label="Red-toned photo of a barbell with weight plates in a gym"></div>
  <svg class="layer layer--base" viewBox="0 0 360 720" aria-hidden="true">
    <path d="M0 0 H360 V62 Q180 122 0 80 Z" fill="#fff"/>
    <rect x="0" y="306" width="360" height="414" fill="#fff"/>
  </svg>
  <div class="photo photo--knee" role="img" aria-label="Black and white photo of hands holding a painful knee, pain area highlighted red"></div>
  <svg class="layer layer--lines" viewBox="0 0 360 720" aria-hidden="true">
    <path d="M0 82 Q180 126 360 62" fill="none" stroke="var(--grey-line)" stroke-width="5"/>
    <path d="M0 362 H360 V392 Q180 350 0 388 Z" fill="#fff"/>
    <path d="M0 388 Q180 350 360 392" fill="none" stroke="var(--red)" stroke-width="4"/>
    <path d="M0 540 Q180 505 360 536 V720 H0 Z" fill="#fff"/>
    <path d="M0 540 Q180 505 360 536" fill="none" stroke="var(--grey-line)" stroke-width="4"/>
  </svg>
  <div class="brand">Brackenridge<br>Strength Studio</div>
  <h2 class="headline--back">HEALTH THROUGH<br>STRENGTH</h2>
  <p class="tagline">You don’t have to live in pain.</p>
  <p class="body-copy body-copy--intro">Strength training has been shown to improve many chronic pain conditions and is now being routinely recommended by medical and health professionals.</p>
  <p class="body-copy body-copy--studio">Our private studio provides high quality strength training by expert strength coaches. We’ve helped countless people improve or eliminate chronic pain, contact us today and find out how we can help you.</p>
  <div class="contact-phone">
    <svg viewBox="0 0 28 28" aria-hidden="true"><circle cx="14" cy="14" r="12" fill="none" stroke="currentColor" stroke-width="2.4"/><path d="M9 8.5c1-1 2-1 2.6 0l1.2 2c.4.7.2 1.3-.4 1.8l-.7.6c.7 1.6 1.8 2.8 3.4 3.5l.6-.7c.5-.6 1.2-.8 1.8-.4l2 1.2c1 .6 1 1.6 0 2.6-1.4 1.3-3.2 1.4-5.6-.3-2.2-1.5-3.8-3.3-4.8-5.6-.9-2.1-.6-3.6.5-4.7z" fill="currentColor"/></svg>
    <span>0452 918 304</span>
  </div>
  <div class="contact-address">
    <svg viewBox="0 0 11 13" aria-hidden="true"><path d="M5.5 12.5S1 7.8 1 5a4.5 4.5 0 0 1 9 0c0 2.8-4.5 7.5-4.5 7.5z" fill="none" stroke="var(--red)" stroke-width="1.3"/><circle cx="5.5" cy="5" r="1.5" fill="var(--red)"/></svg>
    <span>4/63 Juniper Hollow Rd, Brackenridge</span>
  </div>
  <div class="web-band">
    <svg viewBox="0 0 12 12" aria-hidden="true"><circle cx="6" cy="6" r="5.2" fill="none" stroke="#fff" stroke-width="1"/><ellipse cx="6" cy="6" rx="2.3" ry="5.2" fill="none" stroke="#fff" stroke-width="1"/><path d="M0.8 6h10.4" stroke="#fff" stroke-width="1"/></svg>
    <span>www.brackenridgestrengthstudio.example.com.au</span>
  </div>
</section>

</body>
</html>
```